Lumford painting

We are a Painting company. We paint residential and commercial, interior& exterior painting, cabinets refinish,acoustic ceiling painting,popcorn ceiling removal,drywall repair,iron and concrete painting

We don't have any Facebook page or website.

We are a Painting company. We paint residential and commercial, interior& exterior painting, cabinets refinish,acoustic ceiling painting,popcorn ceiling removal,drywall repair,iron and concrete painting We don't have any Facebook page or website.

Requirements
Must have
• I need 200 cards. 50 of with my name Tomás, 50 with Ward 50 with Gavin qnd 50 with boran

```html
<!DOCTYPE html>
<html lang="en">
<head>
<meta charset="utf-8">
<title>Lumford Painting – Business Card</title>
<link href="https://fonts.googleapis.com/css2?family=Montserrat:wght@400;600;700&family=Roboto+Condensed:wght@700&display=swap" rel="stylesheet">
<style>
  :root {
    --purple: #7b2a82;
    --purple-deep: #5e2466;
    --magenta: #b23c8c;
    --orange: #ec6b24;
    --amber: #f4a127;
    --yellow: #f7e925;
    --sky: #1fa3d6;
    --lilac: #8b97cc;
    --white: #ffffff;
    --page: #f1efeb;
  }
  * { margin: 0; padding: 0; box-sizing: border-box; }
  html, body { width: 900px; height: 1200px; overflow: hidden; background: var(--page); }
  body { position: relative; font-family: "Montserrat", sans-serif; }

  .card {
    position: absolute; left: 125px; width: 651px; height: 381px;
    background: var(--white); overflow: hidden;
    box-shadow: 0 6px 18px rgba(0,0,0,0.18);
  }
  .card--front { top: 162px; }
  .card--back { top: 648px; }

  /* splatter artwork areas */
  .splash { position: absolute; }
  .splash--left {
    left: 0; top: 100px; width: 330px; height: 281px;
    background: radial-gradient(ellipse at 20% 60%, var(--purple) 0%, var(--magenta) 40%, var(--lilac) 65%, rgba(255,255,255,0) 78%);
  }
  .splash--corner {
    right: 0; top: 0; width: 130px; height: 110px;
    background: radial-gradient(ellipse at 100% 0%, var(--lilac) 0%, var(--magenta) 30%, rgba(255,255,255,0) 70%);
  }
  .splash--bottom-right {
    right: 0; bottom: 0; width: 190px; height: 150px;
    background: radial-gradient(ellipse at 85% 90%, var(--orange) 0%, var(--amber) 40%, rgba(255,255,255,0) 75%);
  }
  .splash--full {
    inset: 0;
    background: linear-gradient(100deg, var(--amber) 0%, var(--orange) 28%, #f6d98a 48%, var(--magenta) 64%, var(--purple) 80%, var(--sky) 100%);
  }

  /* brand */
  .brand { position: absolute; display: flex; align-items: center; gap: 10px; }
  .brand__mark { background: var(--orange); }
  .brand__name {
    color: var(--purple); font-weight: 700; text-transform: uppercase; line-height: 1;
  }
  .card--front .brand { left: 42px; top: 44px; }
  .card--front .brand__mark { width: 30px; height: 30px; }
  .card--front .brand__name { font-size: 25px; }

  .brand-panel {
    position: absolute; left: 90px; top: 147px; width: 471px; height: 87px;
    background: var(--white); box-shadow: 0 0 18px rgba(255,255,255,0.9);
    display: flex; align-items: center; justify-content: center;
  }
  .brand-panel .brand { position: static; gap: 18px; }
  .brand-panel .brand__mark { width: 48px; height: 48px; }
  .brand-panel .brand__name { font-size: 38px; }

  /* contact */
  .contact { position: absolute; right: 45px; top: 40px; text-align: right; width: 260px; }
  .contact__name {
    font-size: 25px; font-weight: 700; color: var(--orange); letter-spacing: 0.5px;
    padding-bottom: 6px; border-bottom: 1px solid var(--magenta);
  }
  .contact__name span { color: var(--purple); }
  .contact__line {
    display: flex; justify-content: flex-end; align-items: center; gap: 8px;
    color: var(--purple);
  }
  .contact__line--phone { font-size: 21px; font-weight: 700; margin-top: 8px; }
  .contact__line--email { font-size: 13.5px; margin-top: 4px; }
  .contact__line svg { width: 16px; height: 16px; flex: none; }

  .services { position: absolute; right: 45px; top: 155px; list-style: none; text-align: right; }
  .services li {
    display: flex; justify-content: flex-end; align-items: center; gap: 8px;
    font-size: 14.5px; color: var(--purple); height: 27px;
  }
  .services svg { width: 18px; height: 16px; }

  /* banners */
  .banner {
    position: absolute; top: 315px; height: 28px; padding: 0 14px;
    display: flex; align-items: center;
    font-family: "Roboto Condensed", sans-serif; font-weight: 700; font-size: 14.5px;
    text-transform: uppercase;
  }
  .banner--sectors { left: 45px; width: 225px; background: var(--yellow); color: var(--purple); border-left: 4px solid var(--amber); }
  .banner--scope { left: 340px; width: 224px; background: var(--orange); color: var(--white); border-left: 4px solid var(--amber); }
</style>
</head>
<body>

<section class="card card--front">
  <div class="splash splash--left" role="img" aria-label="Paint splatter artwork in purple, magenta and blue"></div>
  <div class="splash splash--corner" role="img" aria-label="Small paint splatter in lilac and purple"></div>
  <div class="splash splash--bottom-right" role="img" aria-label="Paint splatter in orange and amber"></div>

  <div class="brand">
    <span class="brand__mark"></span>
    <span class="brand__name">Lumford<br>Painting</span>
  </div>

  <div class="contact">
    <p class="contact__name">Tomás <span>Arlen</span></p>
    <p class="contact__line contact__line--phone">5550-2841-907
      <svg viewBox="0 0 16 16"><path fill="#ec6b24" d="M2 6c0-2 3-3 6-3s6 1 6 3v1h-3V5.5H5V7H2zM4 8h8l1 6H3z"/></svg>
    </p>
    <p class="contact__line contact__line--email">info@lumfordpainting.com
      <svg viewBox="0 0 16 16"><rect x="1" y="3" width="14" height="10" fill="#ec6b24"/><path d="M1 3l7 6 7-6" stroke="#fff" stroke-width="1.2" fill="none"/></svg>
    </p>
  </div>

  <ul class="services">
    <li>Cabinets refinish <svg viewBox="0 0 18 16"><path d="M2 8l5 5L16 2" stroke="#7b2a82" stroke-width="3" fill="none"/></svg></li>
    <li>Acoustic ceiling painting <svg viewBox="0 0 18 16"><path d="M2 8l5 5L16 2" stroke="#7b2a82" stroke-width="3" fill="none"/></svg></li>
    <li>Popcorn ceiling removal <svg viewBox="0 0 18 16"><path d="M2 8l5 5L16 2" stroke="#7b2a82" stroke-width="3" fill="none"/></svg></li>
    <li>drywall repair <svg viewBox="0 0 18 16"><path d="M2 8l5 5L16 2" stroke="#7b2a82" stroke-width="3" fill="none"/></svg></li>
    <li>Iron and concrete painting <svg viewBox="0 0 18 16"><path d="M2 8l5 5L16 2" stroke="#7b2a82" stroke-width="3" fill="none"/></svg></li>
  </ul>

  <p class="banner banner--sectors">Residential and commercial</p>
  <p class="banner banner--scope">Interior &amp; exterior painting</p>
</section>

<section class="card card--back">
  <div class="splash splash--full" role="img" aria-label="Full-bleed paint splatter artwork in orange, amber, purple, magenta and blue"></div>
  <div class="brand-panel">
    <div class="brand">
      <span class="brand__mark"></span>
      <span class="brand__name">Lumford<br>Painting</span>
    </div>
  </div>
</section>

</body>
</html>
```